Corvenda

I need a professional web site that is directed at the energy industry, Oil, Gas, Mining
I need the website to have the usual pages
1. home page
2. news page.
3. contact us page
4. About us
and a CMS admin section to add further pages and content
Must be Google friendly with SEO facility

Target Market(s)

energy industry, Oil, Gas, Mining

Industry/Entity Type

Industry

Font styles to use
Sans Serif

Colors
faa54b
85cae6
cadf82

Requirements
Must have
• social media icons
site map

```html
<!DOCTYPE html>
<html lang="en">
<head>
<meta charset="utf-8">
<title>Corvenda — Energy Industry</title>
<link href="https://fonts.googleapis.com/css2?family=Raleway:wght@300;400;500;700;800&family=Open+Sans:wght@400;600&display=swap" rel="stylesheet">
<style>
  :root {
    --orange: #faa54b;
    --sky: #85cae6;
    --lime: #cadf82;
    --lime-text: #a8c24a;
    --ink: #222222;
    --body: #555555;
    --muted: #666666;
    --soft-bg: #f5f5f5;
    --footer: #050505;
    --white: #ffffff;
  }
  * { margin: 0; padding: 0; box-sizing: border-box; }
  html, body { width: 980px; height: 1200px; overflow: hidden; background: var(--white); }
  body { position: relative; font-family: "Open Sans", Arial, sans-serif; color: var(--body); }
  .abs { position: absolute; }

  /* Hero */
  .hero-photo { left: 0; top: 0; width: 980px; height: 490px;
    background: linear-gradient(100deg, #8a6a48 0%, #b7b3ae 28%, #b9c6ea 55%, #aebde8 75%, #d7dbe6 100%); }
  .site-header { left: 0; top: 0; width: 980px; height: 76px; background: rgba(255,255,255,0.9); }
  .brand { left: 106px; top: 24px; display: flex; align-items: center; gap: 8px; }
  .brand-name { font-family: "Raleway", sans-serif; font-weight: 800; font-size: 25px; letter-spacing: 1px; color: var(--ink); }
  .brand-dot { width: 12px; height: 12px; border-radius: 50%; background: var(--orange); }
  .main-nav { left: 478px; top: 32px; display: flex; gap: 33px; font-family: "Raleway", sans-serif; font-weight: 500; font-size: 12.5px; color: var(--ink); }
  .hero-caption { left: 97px; top: 220px; width: 325px; height: 129px; background: rgba(202,223,130,0.9); padding: 23px 0 0 24px; }
  .hero-caption h1 { font-family: "Raleway", sans-serif; font-weight: 700; font-size: 23px; color: #1d1d1d; line-height: 1; }
  .hero-caption h2 { font-family: "Raleway", sans-serif; font-weight: 500; font-size: 16px; color: #2a2a2a; margin-top: 9px; }
  .hero-caption p { font-size: 8.3px; line-height: 14px; color: #444; margin-top: 6px; width: 260px; }
  .slide-arrow { top: 232px; }

  /* Intro + industries */
  .industries-band { left: 0; top: 490px; width: 980px; height: 358px; background: linear-gradient(to bottom, var(--white) 60%, var(--soft-bg)); }
  .intro-title { left: 0; top: 530px; width: 980px; text-align: center; font-family: "Raleway", sans-serif; font-weight: 400; font-size: 23px; color: #333; }
  .intro-text { left: 105px; top: 565px; width: 770px; text-align: center; font-size: 11.5px; line-height: 17px; color: var(--muted); }
  .industry-card { top: 641px; width: 185px; }
  .industry-photo { width: 185px; height: 100px; }
  .industry-card h3 { font-family: "Raleway", sans-serif; font-weight: 400; font-size: 14.5px; color: var(--orange); margin-top: 8px; }
  .industry-card p { font-size: 9px; line-height: 14.5px; color: var(--muted); margin-top: 3px; }
  .read-more { display: block; font-size: 10.5px; color: var(--ink); margin-top: 2px; }

  /* About + news */
  .section-title { font-family: "Raleway", sans-serif; font-weight: 400; font-size: 20.5px; color: #222; }
  .about-photo { left: 99px; top: 923px; width: 127px; height: 91px; background: linear-gradient(120deg, #3d86c6 0%, #e8853a 45%, #c9cdd3 100%); }
  .about-lead { left: 236px; top: 920px; width: 330px; font-size: 11px; line-height: 15px; color: #444; }
  .about-body { left: 236px; top: 954px; width: 330px; font-size: 9px; line-height: 15px; color: var(--muted); }
  .about-more { left: 99px; top: 1022px; width: 460px; font-size: 9px; line-height: 15px; color: var(--muted); }
  .news-item { left: 590px; width: 290px; }
  .news-item h4 { font-family: "Open Sans", sans-serif; font-weight: 400; font-size: 11px; color: var(--lime-text); }
  .news-item p { font-size: 8.6px; line-height: 14.5px; color: var(--muted); margin-top: 3px; }

  /* Footer */
  .site-footer { left: 0; top: 1111px; width: 980px; height: 89px; background: var(--footer); }
  .footer-nav { left: 100px; top: 1136px; font-size: 12px; color: var(--white); word-spacing: 2px; }
  .copyright { left: 100px; top: 1158px; font-size: 9px; color: #bbbbbb; }
  .social { left: 810px; top: 1135px; display: flex; gap: 10px; }
  .social-dot { width: 18px; height: 18px; border-radius: 50%; background: #9a9a9a; }
</style>
</head>
<body>
  <div class="abs hero-photo" role="img" aria-label="Oil refinery towers and pipework against a clear blue sky"></div>
  <header class="abs site-header"></header>
  <div class="abs brand"><span class="brand-name">CORVENDA</span><span class="brand-dot"></span></div>
  <nav class="abs main-nav"><span>HOME</span><span>ABOUT US</span><span>INDUSTRIES</span><span>NEWS</span><span>CONTACT US</span></nav>

  <div class="abs hero-caption">
    <h1>SUSPENDISSE MOLESTIE</h1>
    <h2>MAURIS VEL LACUS VITAE FELIS</h2>
    <p>Morbi diam mauris viverra in gravida eu mattis in ante Morbi eget arcu Morbi porta libero id ullamcorper nonummy</p>
  </div>
  <svg class="abs slide-arrow" style="left:48px" width="26" height="60" viewBox="0 0 26 60"><polyline points="24,1 2,30 24,59" fill="none" stroke="#ffffff" stroke-width="2"/></svg>
  <svg class="abs slide-arrow" style="left:890px" width="26" height="60" viewBox="0 0 26 60"><polyline points="2,1 24,30 2,59" fill="none" stroke="#ffffff" stroke-width="2"/></svg>

  <div class="abs industries-band"></div>
  <h2 class="abs intro-title">Vivamus porttitor purus nisi eleifend libero tempus</h2>
  <p class="abs intro-text">Morbi diam mauris viverra in gravida eu mattis in ante Morbi eget arcu Morbi porta libero id ullamcorper nonummy nibh ligula pulvinar metus eget consectetuer augue nisi quis lacus Ut ac mi quis lacus mollis aliquam Curabitur</p>

  <article class="abs industry-card" style="left:100px">
    <div class="industry-photo" role="img" aria-label="Oil plant lit up at dusk" style="background:linear-gradient(to bottom,#4a6fb0,#2d3e5a 55%,#1b2a36)"></div>
    <h3>OIL INDUSTRY</h3>
    <p>Etiam est nunc venenatis in tristique eu imperdiet ac nisl Cum sociis natoque</p>
    <span class="read-more">Read More</span>
  </article>
  <article class="abs industry-card" style="left:298px">
    <div class="industry-photo" role="img" aria-label="Electricity pylons under a vivid sky" style="background:linear-gradient(160deg,#1f4fa8,#5e8fe0 50%,#e08a9a)"></div>
    <h3>ENERGY INDUSTRY</h3>
    <p>Etiam est nunc venenatis in tristique eu imperdiet ac nisl Cum sociis natoque</p>
    <span class="read-more">Read More</span>
  </article>
  <article class="abs industry-card" style="left:496px">
    <div class="industry-photo" role="img" aria-label="Gas processing plant glowing at night" style="background:linear-gradient(to bottom,#2a1a0c,#8a4a10 55%,#d98a20)"></div>
    <h3>GAS INDUSTRY</h3>
    <p>Etiam est nunc venenatis in tristique eu imperdiet ac nisl Cum sociis natoque</p>
    <span class="read-more">Read More</span>
  </article>
  <article class="abs industry-card" style="left:695px">
    <div class="industry-photo" role="img" aria-label="Mining dump trucks in a quarry" style="background:linear-gradient(to bottom,#9aa0a6,#7a7a76 55%,#8e7a50)"></div>
    <h3>MINING INDUSTRY</h3>
    <p>Etiam est nunc venenatis in tristique eu imperdiet ac nisl Cum sociis natoque</p>
    <span class="read-more">Read More</span>
  </article>

  <h2 class="abs section-title" style="left:98px;top:888px">About Our Company</h2>
  <div class="abs about-photo" role="img" aria-label="Two engineers in safety gear at a refinery"></div>
  <p class="abs about-lead">Mauris vel lacus vitae felis vestibulum volutpat Etiam est nunc venena tis in tristique eu imperdiet</p>
  <p class="abs about-body">ac nisl Cum sociis natoque penatibus et magnis dis parturient montes nascetur ridiculus mus In iaculis facilisis massa Suspendisse quam leo molestie sed luctus quis feugiat in pede Fusce tellus Sed metus augue convallis et vehicula ut pulvinar eu ante Integer orci tellus tristique vitae consequat nec</p>
  <p class="abs about-more">Morbi ornare gravida elit Integer congue augue et malesuada iaculis ipsum dui aliquet felis at cursus magna nisl nec elit Praesent elementum elit at tellus nec ultricies sit amet porttitor mattis enim In massa libero interdum nec interdum vel blandit sed nulla In ullamcorper est eget tempor cursus neque</p>

  <h2 class="abs section-title" style="left:590px;top:890px">Latest News</h2>
  <div class="abs news-item" style="top:919px">
    <h4>Morbi ornare gravida elit</h4>
    <p>Morbi porta libero id ullamcorper nonummy nibh ligula pulvinar metus eget consectetuer augue nisi quis lacus Ut ac mi quis lacus mollis</p>
  </div>
  <div class="abs news-item" style="top:985px">
    <h4>Curabitur iaculis tempus</h4>
    <p>Morbi ornare gravida elit Integer congue augue et malesuada iaculis ipsum dui aliquet felis at cursus magna nisl nec elit Praesent elementum elit at tellus nec ultricies sit amet porttitor mattis enim</p>
  </div>

  <footer class="abs site-footer"></footer>
  <nav class="abs footer-nav">Home &nbsp;| &nbsp;About us &nbsp;| &nbsp;Industries &nbsp;| &nbsp;News &nbsp;| &nbsp;Contact us &nbsp;| &nbsp;Sitemap</nav>
  <p class="abs copyright">© 2014 Company Name &nbsp;All right reserved &nbsp;Term of Use</p>
  <div class="abs social">
    <span class="social-dot" role="img" aria-label="Social network link"></span>
    <span class="social-dot" role="img" aria-label="Social network link"></span>
    <span class="social-dot" role="img" aria-label="Social network link"></span>
  </div>
</body>
</html>
```